The Yarrawin Pet Groomer

I have a logo which I designed myself ( I tried a contest and it did not work out well..not on this site) The logo needs some tweaking for example "THE" needs to be put above "YARRAWIN" in line with the D (on top)and it needs to be going across sideways.Also the dog is not exactly in the middle.
Also on the card I would like my name written in a simple running writing script
Marnie

Then in plain writing:
27B Fenwick St Yarrawin NSW 2848
Ph. 6319 5057
On the back:
Your next appointment:
...........................................

Pet bathing, clipping and styling

Pet

Must have
• The logo going across lengthways and changed a bit (as explained above)

```html
<!DOCTYPE html>
<html lang="en">
<head>
<meta charset="utf-8">
<title>The Yarrawin Pet Groomer – Business Card</title>
<link rel="stylesheet" href="https://fonts.googleapis.com/css2?family=PT+Sans:wght@400;700&family=Dancing+Script:wght@600&display=swap">
<style>
  :root {
    --page-bg: #ece9e4;
    --card-front: #050505;
    --card-back: #ffffff;
    --ink-light: #ffffff;
    --ink-dark: #111111;
    --accent-red: #e3262b;
    --faint-grey: #ececec;
    --rule-light: #dcdcdc;
  }
  * { margin: 0; padding: 0; box-sizing: border-box; }
  html, body {
    width: 978px; height: 1200px; overflow: hidden;
    background: var(--page-bg);
    font-family: "PT Sans", Arial, sans-serif;
  }
  .canvas { position: relative; width: 978px; height: 1200px; }

  .card {
    position: absolute; left: 89px; width: 800px; height: 450px;
    border-radius: 28px;
    box-shadow: 0 8px 22px rgba(0,0,0,0.25);
    overflow: hidden;
  }
  .card--front { top: 80px; background: var(--card-front); color: var(--ink-light); }
  .card--back  { top: 640px; background: var(--card-back); color: var(--ink-dark); }

  .owner-name {
    position: absolute; top: 40px; right: 70px;
    font-family: "Dancing Script", cursive;
    font-weight: 600; font-size: 44px; line-height: 1.2;
    color: var(--accent-red);
  }
  .brand-name {
    position: absolute; left: 80px; right: 40px; top: 218px;
    text-align: center;
    font-weight: 700; font-size: 50px; line-height: 1.2; letter-spacing: 1px;
    color: var(--ink-light);
  }
  .front-rule {
    position: absolute; left: 80px; right: 40px; top: 320px;
    border-top: 1.5px solid var(--rule-light);
  }
  .contact-line {
    position: absolute; left: 80px; right: 40px; top: 352px;
    text-align: center; font-size: 20px; line-height: 1.2; color: var(--ink-light);
  }

  .faint-mark {
    position: absolute; left: 290px; top: 90px;
  }
  .appointment-label {
    position: absolute; left: 0; right: 0; top: 46px;
    text-align: center; font-weight: 700; font-size: 20px; line-height: 1.2;
  }
  .appointment-line {
    position: absolute; left: 290px; width: 230px; top: 110px;
    border-top: 1.5px dashed #555;
  }
  .back-rule {
    position: absolute; left: 40px; right: 40px;
    border-top: 1.5px solid var(--ink-dark);
  }
  .back-rule--upper { top: 290px; }
  .back-rule--lower { top: 400px; }
  .brand-name--small {
    position: absolute; left: 0; right: 0; top: 300px;
    text-align: center; font-weight: 700; font-size: 20px; line-height: 1.2;
    color: var(--ink-dark);
  }
  .services {
    position: absolute; left: 0; right: 0; top: 340px;
    text-align: center; font-size: 28px; line-height: 1.2;
  }
</style>
</head>
<body>
<main class="canvas">
  <section class="card card--front" aria-label="Card front">
    <p class="owner-name">Marnie</p>
    <h1 class="brand-name">The Yarrawin Pet Groomer</h1>
    <div class="front-rule"></div>
    <p class="contact-line">27B Fenwick St Yarrawin NSW 2848 &nbsp;|&nbsp; Ph. 6319 5057</p>
  </section>

  <section class="card card--back" aria-label="Card back">
    <svg class="faint-mark" width="220" height="190" viewBox="0 0 220 190" role="img" aria-label="Faint brand decoration area">
      <rect x="10" y="5" width="200" height="180" rx="90" fill="var(--faint-grey)"/>
    </svg>
    <p class="appointment-label">Your next appointment :</p>
    <div class="appointment-line"></div>
    <div class="back-rule back-rule--upper"></div>
    <p class="brand-name--small">The Yarrawin Pet Groomer</p>
    <p class="services">Pet bathing, clipping and styling</p>
    <div class="back-rule back-rule--lower"></div>
  </section>
</main>
</body>
</html>
```